Striking new Advert required for Commercial Real Estate Agency

We need a a NEW newspaper advertisement for the marketing of a large commercial property (a Backpackers lodge)

Dimensions are to be width of 101mm and height of 100mm (10cms)

Our key design statement for this advert is clean, modern and minimalist design, with accents of 'HOT PINK' colour to remove it from looking too boring, perhaps in the area of the contact icons. The heirachy of the advert is outlined in the attached ADVERTISEMENT TEXT FILE.

Our company name is THE VANTREL COLLECTIVE, and we want our brand to appear professional yet classy in it's design style (sort of like an advertising or design agency)

We have two logo options below, one more square in its layout (which we prefer) and the other more rectangular, which may be better suited for the layout. We are not adverse to the logo being reversed (white text on black), along with other key element areas such as the main advert heading and the "FOR SALE" part, and think this would be a good option.
There are two photos attached to be included in the advert.

We have attached an example of an old advert that we did, which we DID NOT LIKE, and which was for a smaller width than the one we need (it is only 65% of the width of this one). WE have also atached a file showing layout of some of our competitors adverts, which we dont think are too good either.

We are really open for ideas, but have time pressures, so please come back with any questions as soon as you can, if needed.

Thank you
Updates

Thank you for the great and diverse designs. There are a few standout options, but one style that we prefer most.

Target Market(s)

We are wanting this newspaper advertisement to attract interest from real estat e developers, investors and motel/lodge owners, along with other high nett worth individuals

Industry/Entity Type

Real Estate

Font styles to use
Serif
Sans Serif

Colors
1b1b1b
a54499
474747
fbfbfb

Requirements
Must have
• Clean modern look, predominantly monochromatic or black and white, with the hot pink accent somewhere, as mentioned above.
• All the contents of the TEXT provided, perhaps with additional space to add a little more if needed, Please advise if you think we dont have enough space for all of the TEXT
Should not have
• Script like fonts
• Cartoonish characters
• a 'cheap' look

```html
<!DOCTYPE html>
<html lang="en">
<head>
<meta charset="utf-8">
<title>Mount Victoria Land Grab – For Sale</title>
<link rel="stylesheet" href="https://fonts.googleapis.com/css2?family=Open+Sans:wdth,wght@75..100,300..800&display=swap">
<style>
  :root {
    --ink: #1b1b1b;
    --pink: #a54499;
    --slate: #3d3d3d;
    --grey: #474747;
    --paper: #fbfbfb;
    --white: #ffffff;
  }
  * { margin: 0; padding: 0; box-sizing: border-box; }
  html, body { width: 1200px; height: 1200px; overflow: hidden; background: var(--white); }
  body { font-family: "Open Sans", Arial, sans-serif; color: var(--ink); }

  .advert {
    position: absolute; left: 0; top: 5px;
    width: 940px; height: 932px;
    background: var(--white);
    transform: scale(1.2766); transform-origin: 0 0;
    overflow: hidden;
  }
  .abs { position: absolute; }

  .header-shapes { left: 0; top: 0; width: 940px; height: 150px; }
  .for-sale {
    left: 34px; top: 4px; color: var(--white);
    font-size: 136px; font-weight: 700; font-stretch: 85%;
    line-height: 140px; letter-spacing: 1px;
  }
  .headline {
    left: 626px; top: 16px; color: var(--white);
    font-size: 43px; font-weight: 400; line-height: 48px;
  }
  .address {
    left: 0; width: 940px; top: 160px; text-align: center;
    font-size: 34px; font-weight: 700; font-stretch: 78%; color: var(--ink);
  }
  .photo { top: 210px; height: 295px; }
  .photo-building { left: 0; width: 465px; background: linear-gradient(180deg, #5a95d8 0%, #a9c9e8 35%, #e9eef2 55%, #6f8a4c 100%); }
  .photo-aerial { left: 476px; width: 464px; background: linear-gradient(160deg, #9aa88a 0%, #c8ccc4 40%, #8f9a86 70%, #5f7a3c 100%); }

  .tagline-band {
    left: 0; top: 505px; width: 940px; height: 67px; background: var(--slate);
    color: var(--white); text-align: center;
    font-size: 33px; font-weight: 600; font-stretch: 78%; line-height: 67px;
  }
  .details { left: 30px; top: 588px; width: 895px; }
  .details-intro {
    color: var(--pink); font-size: 23px; font-weight: 700; font-stretch: 75%;
    line-height: 32px; margin-bottom: 4px; white-space: nowrap;
  }
  .details-list { list-style: none; font-size: 15.5px; line-height: 18px; color: var(--ink); }
  .details-list li { position: relative; padding-left: 10px; margin-bottom: 10px; }
  .details-list li:last-child { margin-bottom: 0; }
  .details-list li::before { content: "•"; position: absolute; left: 0; font-size: 11px; }

  .tender-shapes { left: 0; top: 738px; width: 940px; height: 59px; }
  .tender {
    left: 22px; top: 738px; color: var(--white); line-height: 58px;
    font-size: 44px; font-weight: 600; font-stretch: 78%;
  }
  .tender small { font-size: 31px; font-weight: 600; }
  .web {
    left: 520px; top: 753px; color: var(--white); line-height: 44px;
    font-size: 32px; font-weight: 700; font-stretch: 78%;
  }

  .footer { left: 0; top: 797px; width: 940px; height: 135px; background: var(--ink); }
  .brand-mark { left: 23px; top: 30px; width: 75px; height: 75px; border: 3px solid var(--white); }
  .brand-rule { left: 117px; top: 22px; width: 2px; height: 88px; background: var(--white); }
  .brand-name { left: 137px; top: 30px; color: var(--white); font-weight: 400; line-height: 1; }
  .brand-name .small { display: block; font-size: 26px; margin-bottom: 8px; }
  .brand-name .large { display: block; font-size: 34px; }
  .footer-rule { left: 532px; top: 20px; width: 2px; height: 96px; background: var(--white); }
  .agent { left: 565px; top: 18px; color: var(--white); }
  .agent-name { font-size: 30px; font-weight: 400; line-height: 40px; margin-bottom: 6px; }
  .agent-line {
    display: flex; align-items: center; gap: 8px;
    font-size: 21px; font-weight: 600; font-stretch: 78%; line-height: 29px;
  }
  .agent-line svg { width: 20px; height: 20px; fill: var(--pink); }
  .sep { margin: 0 4px; }
</style>
</head>
<body>
<main class="advert">
  <svg class="abs header-shapes" viewBox="0 0 940 150" aria-hidden="true">
    <polygon points="0,0 612,0 548,150 0,150" fill="var(--pink)"/>
    <polygon points="626,0 940,0 940,128 566,128" fill="var(--ink)"/>
  </svg>
  <h1 class="abs for-sale">FOR SALE</h1>
  <p class="abs headline">Mount Victoria<br>Land Grab</p>

  <h2 class="abs address">Marlowe’s Lodge, 27 Kestrel Street, Mount Victoria</h2>

  <div class="abs photo photo-building" role="img" aria-label="Photo of the two-storey white weatherboard lodge from street level"></div>
  <div class="abs photo photo-aerial" role="img" aria-label="Aerial photo of the lodge, its car park and surrounding suburb"></div>

  <p class="abs tagline-band">This Old Beauty has served many, and is now ripe for development.</p>

  <section class="abs details">
    <p class="details-intro">One of Mt Vic’s largest land areas, now offered with vacant possession, with key details being:</p>
    <ul class="details-list">
      <li>Large Land area of 2076m² with elevated sunny position and great outlook + access from Ardent Street.</li>
      <li>Existing Backpackers Lodge of 970m² providing multiple rooms with amenity areas.</li>
      <li>Four adjacent sites also available, taking total land area to 4452m², an unprecedented Land Offering in<br>this popular cuity fringe location.</li>
    </ul>
  </section>

  <svg class="abs tender-shapes" viewBox="0 0 940 59" aria-hidden="true">
    <polygon points="0,0 500,0 470,59 0,59" fill="var(--slate)"/>
    <polygon points="494,17 940,17 940,57 475,57" fill="var(--pink)"/>
  </svg>
  <p class="abs tender">Now Selling <small>by Closed Tender</small></p>
  <p class="abs web">www.vantrelcollective.co.nz</p>

  <footer class="abs footer">
    <div class="abs brand-mark"></div>
    <div class="abs brand-rule"></div>
    <p class="abs brand-name"><span class="small">THE</span><span class="large">VANTREL COLLECTIVE</span></p>
    <div class="abs footer-rule"></div>
    <div class="abs agent">
      <p class="agent-name">Miles Harrow</p>
      <p class="agent-line">
        <svg viewBox="0 0 24 24" aria-hidden="true"><path d="M6.6 10.8a15.1 15.1 0 0 0 6.6 6.6l2.2-2.2c.3-.3.7-.4 1-.2 1.1.4 2.3.6 3.6.6.6 0 1 .4 1 1V20c0 .6-.4 1-1 1A17 17 0 0 1 3 4c0-.6.4-1 1-1h3.5c.6 0 1 .4 1 1 0 1.3.2 2.5.6 3.6.1.3 0 .7-.2 1z"/></svg>
        (04) 555 0142 <span class="sep">|</span>
        <svg viewBox="0 0 24 24" aria-hidden="true"><path d="M7 1h10a2 2 0 0 1 2 2v18a2 2 0 0 1-2 2H7a2 2 0 0 1-2-2V3a2 2 0 0 1 2-2zm0 3v14h10V4zm5 15.5a1.2 1.2 0 1 0 0 2.4 1.2 1.2 0 0 0 0-2.4z"/></svg>
        (021) 555 718
      </p>
      <p class="agent-line">
        <svg viewBox="0 0 24 24" aria-hidden="true"><path d="M2 5h20v14H2zm2 2v.4l8 5.2 8-5.2V7zm0 2.8V17h16V9.8l-8 5.2z"/></svg>
        miles@vantrelcollective.co.nz
      </p>
    </div>
  </footer>
</main>
</body>
</html>
```